DESIGN A LEAFLET FOR A CANNABIS CLUB!!

We need a leaflet design for a cannabis club based in the United Kingdom, called Silver Brook Cannabis Club

PLEASE, FEEL FREE TO ADD YOUR OWN INFO ETC

Just want attention drawn to the PICSHARE/WEBSITE whilst looking semi-professional

LEGALIZE IT (title)

Government officials are denying your right to access legal Cannabis.

Over Thirty-five countries already have legal access in one form or another... What are we waiting for ?

I'd ideally like the leaflet to be A6 size

"PICSHARE LOGO": Silverbrookcannabisclub
*MUST SEE*
"FRIENDPAGE LOGO": Silverbrookcannabisclub
WEB: www.silverbrookcannabisclub.example

Check us out!
*Cannabis Discussion Forum*
*Weed related news*
*Awesome Documentaries*

Industry/Entity Type

Club

Requirements
Must have
• Please use my logo on leaflet somewhere, feel free to re-size it
• Back of leaflet to just have my cannabis logo in large with green and smoky background
Nice to have
• PLEASE, FEEL FREE TO ADD YOUR OWN INFO ETC
• Just want attention drawn to PICSHARE/WEBSITE whilst looking semi-professional
Should not have
• Plain, boring, minimal effort

```html
<!DOCTYPE html>
<html lang="en">
<head>
<meta charset="utf-8">
<title>Silver Brook Cannabis Club – Leaflet</title>
<link href="https://fonts.googleapis.com/css2?family=Bebas+Neue&family=Ubuntu:ital,wght@0,400;0,500;0,700;1,400&display=swap" rel="stylesheet">
<style>
  :root{
    --green:#2f8c3c;
    --green-dark:#1e6b2b;
    --brown:#8b5226;
    --red:#c9262c;
    --teal:#2c7f92;
    --paper:#f4f4f4;
    --ink:#333;
    --white:#fff;
  }
  html,body{margin:0;padding:0;width:1200px;height:1200px;overflow:hidden;background:#fff;}
  body{position:relative;font-family:"Ubuntu",sans-serif;}
  .leaflet{position:absolute;top:205px;width:570px;height:805px;transform:scale(0.857);transform-origin:0 0;overflow:hidden;background:linear-gradient(160deg,#fff 0%,var(--paper) 100%);box-shadow:0 2px 8px rgba(0,0,0,.15);}
  .leaflet--front{left:75px;}
  .leaflet--back{left:646px;}
  .front-shapes{position:absolute;inset:0;}
  .club-name{position:absolute;display:flex;align-items:center;gap:10px;font-family:"Ubuntu",sans-serif;font-weight:700;color:var(--green-dark);line-height:1.05;white-space:nowrap;}
  .club-name__dot{flex:none;border-radius:50%;background:#a7a7a7;}
  .front-name{left:155px;top:70px;font-size:26px;}
  .front-name .club-name__dot{width:34px;height:34px;}
  .members-badge{position:absolute;left:394px;top:60px;width:134px;height:134px;border-radius:50%;background:var(--green);box-shadow:0 0 0 5px #56a64a;display:flex;align-items:center;justify-content:center;text-align:center;font-family:"Bebas Neue",sans-serif;color:#fff;font-size:30px;line-height:.9;}
  .headline{position:absolute;left:34px;top:246px;margin:0;font-family:"Bebas Neue",sans-serif;font-weight:400;font-size:64px;color:#fff;letter-spacing:-1px;line-height:1;}
  .intro{position:absolute;left:37px;top:311px;margin:0;font-size:15.5px;line-height:20px;color:#fff;white-space:nowrap;}
  .web-bar{position:absolute;left:0;top:474px;width:335px;height:33px;background:var(--brown);border-radius:0 8px 8px 0;color:#fff;font-size:15.5px;line-height:33px;padding-left:30px;box-sizing:border-box;white-space:nowrap;}
  .features{position:absolute;left:34px;top:522px;margin:0;padding:0;list-style:none;}
  .features li{font-style:italic;color:#fff;font-size:17px;line-height:29px;display:flex;align-items:center;gap:10px;}
  .features li::before{content:"";width:10px;height:10px;background:#fff;}
  .socials{position:absolute;left:60px;top:628px;display:flex;gap:24px;}
  .social{display:flex;align-items:center;gap:6px;color:#fff;font-size:13px;font-weight:500;}
  .social__square{width:26px;height:26px;background:#fff;border-radius:4px;}
  .handle{position:absolute;left:0;width:270px;top:682px;text-align:center;color:#fff;font-size:13px;font-weight:500;}
  .strain-table{position:absolute;left:342px;top:259px;width:182px;height:189px;border:4px solid var(--brown);border-radius:8px;background:#fff;box-sizing:border-box;overflow:hidden;display:flex;flex-direction:column;}
  .strain-table__title{font-size:13px;text-align:center;color:var(--ink);line-height:16px;}
  .strain-table__cols{flex:1;display:grid;grid-template-columns:1fr 1fr;gap:2px;}
  .strain-col{display:flex;flex-direction:column;color:#fff;font-size:6px;line-height:7px;}
  .strain-col--sativa{background:var(--red);}
  .strain-col--indica{background:var(--teal);}
  .strain-col__head{font-size:12px;line-height:15px;text-align:center;border-bottom:1px solid rgba(255,255,255,.6);}
  .strain-col__row{flex:1;display:flex;align-items:center;padding:0 5px;border-bottom:1px solid rgba(255,255,255,.35);}
  .photo{position:absolute;border:4px solid var(--brown);border-radius:8px;box-sizing:border-box;}
  .photo--display{left:344px;top:462px;width:178px;height:118px;background:linear-gradient(150deg,#6d6a4e 0%,#b6b28d 45%,#8c8a66 100%);}
  .photo--jars{left:306px;top:610px;width:220px;height:148px;background:linear-gradient(180deg,#3f4a33 0%,#6d7a5a 45%,#9a9a88 55%,#3c4a30 100%);}
  .back-wash{position:absolute;inset:0;background:
      radial-gradient(ellipse 80% 45% at 80% 95%,rgba(140,200,90,.55),transparent 70%),
      radial-gradient(ellipse 60% 35% at 30% 100%,rgba(170,215,130,.45),transparent 70%),
      linear-gradient(160deg,#fff 0%,#eef3ea 60%,#d8ebc4 100%);}
  .back-name{left:0;width:570px;justify-content:center;top:220px;font-size:40px;}
  .back-name .club-name__dot{width:48px;height:48px;}
</style>
</head>
<body>

<section class="leaflet leaflet--front">
  <svg class="front-shapes" viewBox="0 0 570 805" width="570" height="805" aria-hidden="true">
    <polygon points="0,107 265,258 300,690 0,775" fill="var(--green)"/>
    <polygon points="265,258 570,236 570,300" fill="var(--green-dark)"/>
    <polygon points="262,262 275,262 330,680 318,684" fill="var(--brown)"/>
    <polygon points="0,780 300,694 300,700 0,790" fill="#fff"/>
    <rect x="0" y="776" width="570" height="5" fill="var(--brown)"/>
    <rect x="0" y="786" width="570" height="21" fill="var(--brown)"/>
  </svg>

  <div class="club-name front-name"><span class="club-name__dot"></span><span>Silver Brook<br>Cannabis Club</span></div>
  <div class="members-badge">PRIVATE<br>MEMBERS<br>CLUB</div>

  <h1 class="headline">LEGALIZE IT</h1>
  <p class="intro">Government officials are<br>denying your right to<br>access legal Cannabis.<br>Over Thirty-five countries<br>already have legal access<br>in one form or another...<br>What are we waiting for ?</p>

  <div class="web-bar">www.silverbrookcannabisclub.example</div>

  <ul class="features">
    <li>Cannabis discussion Forum</li>
    <li>Cannabis related news articles</li>
    <li>Awesome documentaries</li>
  </ul>

  <div class="socials">
    <span class="social"><span class="social__square"></span>PicShare</span>
    <span class="social"><span class="social__square"></span>FriendPage</span>
  </div>
  <div class="handle">SILVERBROOKCANNABISCLUB</div>

  <div class="strain-table">
    <div class="strain-table__title">KNOW YOUR CANNABIS</div>
    <div class="strain-table__cols">
      <div class="strain-col strain-col--sativa">
        <div class="strain-col__head">SATIVA</div>
        <div class="strain-col__row">TALLER, LEAVES LONGER &amp; THINNER</div>
        <div class="strain-col__row">HEAD HIGH</div>
        <div class="strain-col__row">ALERTNESS</div>
        <div class="strain-col__row">UPLIFTING &amp; EUPHORIC</div>
        <div class="strain-col__row">CREATIVITY</div>
        <div class="strain-col__row">INCREASED ENERGY</div>
        <div class="strain-col__row">BEST FOR DAYTIME USE</div>
      </div>
      <div class="strain-col strain-col--indica">
        <div class="strain-col__head">INDICA</div>
        <div class="strain-col__row">SHORTER, LEAVES SHORTER &amp; WIDER</div>
        <div class="strain-col__row">BODY HIGH</div>
        <div class="strain-col__row">RELAXATION</div>
        <div class="strain-col__row">APPETITE STIMULATOR</div>
        <div class="strain-col__row">SLEEP AID</div>
        <div class="strain-col__row">PAIN RELIEF</div>
        <div class="strain-col__row">BEST FOR NIGHTTIME USE</div>
      </div>
    </div>
  </div>

  <div class="photo photo--display" role="img" aria-label="Photo of cannabis buds in labelled display dishes"></div>
  <div class="photo photo--jars" role="img" aria-label="Photo of glass jars of cannabis on shelves"></div>
</section>

<section class="leaflet leaflet--back">
  <div class="back-wash" role="img" aria-label="Soft green smoky wave background"></div>
  <div class="club-name back-name"><span class="club-name__dot"></span><span>Silver Brook<br>Cannabis Club</span></div>
</section>

</body>
</html>
```